Science News Webpage Design

Quarry Lantern Works gGmbH is a non-profit organisation developing apps for scientists. Our main project is a scientific platform you can visit at quarrylantern.net.

The QLW platform consists of multiple modules. We are now considering to spin out one of the modules (Tides & Notes) and create a separate web application with focus on latest science news that enables scientists to easily contribute by writing their own articles and commentaries.

For this news website, we need someone to design the homepage and three other templates.

We prepared a set of files consisting of a more detailed brief and also a couple of wire-frames.

Please check these files and get in touch with us in case you have questions or in case something is unclear.
Updates

Hello everyone,

Just a short note. Although I have indicated in the brief that this project is a spin-out from another platform, you shouldn't feel restricted to design and color combinations of that other site. We are really trying to make something new here, and the design can be completely different.

I also attached a new file. The working title of the project is "wonder unwrapped". Although we haven't decided on the final name, you can use this png as logo.

Cheers,
Toma

Updated home page wireframe to include all links in the menu (since there are more links than originally depicted and this obviously influences design).

Industry/Entity Type

Non-Profit

```html
<!DOCTYPE html>
<html lang="en">
<head>
<meta charset="utf-8">
<title>wonder unwrapped — science news</title>
<link rel="stylesheet" href="https://fonts.googleapis.com/css2?family=Open+Sans:wght@400;600;700&display=swap">
<style>
:root{
  --red:#e8432e;
  --ink:#222;
  --text:#555;
  --muted:#8a8a8a;
  --line:#cfcfcf;
  --nav:#2a2a2a;
  --panel:#f0f0f0;
  --footer:#ececec;
  --bottom:#2b2b2b;
  --cream:#fbf3ea;
}
*{box-sizing:border-box;margin:0;padding:0}
html,body{width:1200px;height:4327px;overflow:hidden;background:#fff}
body{font-family:"Open Sans",Arial,sans-serif;color:var(--text);position:relative}
a{color:inherit;text-decoration:none}
.abs{position:absolute}

.top-ad{left:225px;top:0;width:770px;height:100px;display:flex;background:#fff}
.top-ad .headline{width:250px;background:#f29a1f;color:#fff;font-weight:700;font-size:22px;line-height:27px;padding:20px 14px}
.top-ad .kids{flex:1;background:linear-gradient(90deg,#f6c94c,#e9a9c9,#8fc8e8)}
.top-ad .info{width:200px;background:#f07b22;color:#fff;font-weight:700;font-size:16px;padding:22px 12px;line-height:26px;white-space:nowrap;overflow:hidden}

.brand{left:100px;top:118px}
.brand .name{font-size:46px;font-weight:700;color:var(--ink);letter-spacing:-1px;line-height:54px}
.brand .tag{font-size:12px;color:var(--muted)}
.account{left:940px;top:120px;display:flex;gap:8px}
.btn{font-size:12px;font-weight:700;padding:6px 12px;color:#fff;background:var(--red)}
.btn.alt{background:#d6d6d6;color:#444}
.follow{left:902px;top:162px;display:flex;align-items:center;gap:6px;font-size:11px;color:var(--muted)}
.follow i{display:block;width:22px;height:22px;background:#3a3a3a}

.nav{left:0;top:219px;width:1200px;height:41px;background:var(--nav)}
.nav ul{list-style:none;display:flex;margin-left:100px;height:41px;align-items:center}
.nav li{color:#ddd;font-size:14px;padding:0 13px;height:41px;line-height:41px}
.nav li.on{color:var(--red);border-bottom:3px solid var(--red)}

.shead{display:flex;align-items:center;height:30px}
.shead h2{font-size:22px;font-weight:600;color:var(--red);text-transform:uppercase;margin-right:8px;white-space:nowrap}
.shead .rule{flex:1;height:1px;background:var(--line);position:relative}
.shead .rule::after{content:"";position:absolute;right:0;top:-6px;border-left:9px solid #999;border-top:6px solid transparent;border-bottom:6px solid transparent}

.photo{display:block}
.card h3{font-size:16px;font-weight:700;color:var(--ink);line-height:24px;margin-top:18px}
.meta{font-size:11px;color:var(--muted);margin-top:6px;font-style:italic}
.meta b{color:var(--red);font-weight:400}
.card p{font-size:13px;line-height:19px;margin-top:8px}
.more{display:block;font-size:12px;color:var(--red);font-weight:600;margin-top:14px}

.side-panel{background:var(--panel);padding:16px}
.side-panel .shead h2{font-size:21px}
.mini{display:flex;gap:14px;margin-top:20px}
.mini .photo{width:110px;height:90px;flex:none}
.mini h4{font-size:14px;font-weight:600;color:var(--ink);line-height:19px}

.sponsored{left:0;top:1486px;width:1200px;height:332px;background:linear-gradient(180deg,var(--cream),#fff)}
.sp-grid{display:flex;gap:26px;margin-top:22px}
.sp-item{width:230px}
.sp-item .photo{height:125px}
.sp-item p{font-size:12px;color:#999;line-height:17px;margin-top:10px}
.sp-item .by{font-size:12px;color:var(--ink);margin-top:8px;line-height:17px}

.partners{display:flex;justify-content:space-between;margin-top:26px;align-items:center}
.partners span{font-size:20px;font-weight:700;color:#8a8a8a}
.partners .chip{width:88px;height:38px;background:#bdbdbd;border-radius:8px;display:flex;align-items:center;justify-content:center;color:#fff;font-size:14px}

.footer{left:0;top:4010px;width:1200px;height:254px;background:var(--footer)}
.footer h5{font-size:16px;font-weight:600;color:var(--ink)}
.links{display:flex;gap:44px;margin-top:18px}
.links ul{list-style:none;font-size:11px;line-height:21px}
.links li::before{content:"› ";color:var(--muted)}
.field{width:230px;height:28px;border:1px solid #ccc;background:#fff;font-size:11px;padding:6px 8px;margin-top:12px;color:#555}
.submit{display:inline-block;margin-top:10px;margin-left:168px;background:#444;color:#fff;font-size:11px;font-weight:700;padding:6px 10px}
.social{list-style:none;margin-top:14px}
.social li{display:flex;align-items:center;gap:10px;font-size:12px;height:36px}
.social i{width:26px;height:26px;background:#4d6fa8;display:block}
.social b{color:#3b6db3;font-weight:600;font-size:14px}
.bottom{left:0;top:4264px;width:1200px;height:63px;background:var(--bottom);color:#aaa;font-size:11px;text-align:center;line-height:63px}
</style>
</head>
<body>

<div class="abs top-ad">
  <div class="headline">MAKE ROOM FOR<br>FAMILY TIME</div>
  <div class="kids" role="img" aria-label="Cartoon illustration of children playing"></div>
  <div class="info">555-0142<br>fatherpath.example</div>
</div>

<header>
  <div class="abs brand">
    <div class="name">wonder unwrapped</div>
    <div class="tag">Science, health and technology news</div>
  </div>
  <div class="abs account"><a class="btn">SIGN IN</a><a class="btn alt">SIGN UP</a></div>
  <div class="abs follow">FOLLOW US <i></i><i></i><i></i><i></i></div>
</header>

<nav class="abs nav"><ul>
  <li class="on">LATEST</li><li>BIOLOGY</li><li>CHEMISTRY</li><li>PHYSICS</li><li>COMPUTATION</li><li>EARTH</li><li>TECHNOLOGY</li><li>HEALTH</li><li>SOCIAL</li><li>MORE NEWS?</li><li>QUESTIONS?</li>
</ul></nav>

<section class="abs" style="left:100px;top:288px;width:656px">
  <div class="shead"><h2>Latest</h2><div class="rule"></div></div>
  <article class="card abs" style="left:0;top:47px;width:290px">
    <div class="photo" style="height:175px;background:radial-gradient(circle at 40% 60%,#4a7fd0,#0d1a3a)" role="img" aria-label="Businessman touching a glowing digital interface"></div>
    <h3>Wormholes in Host Defense: How Helminths Manipulate Host Tissues to Survive and Reproduce..</h3>
    <div class="meta">Genetic Engineering | Article | <b>By R.Ellison</b></div>
    <p>Aliquam molestie, mi et imperdiet euismod, dui purus auctor tellus, et interdum lacus lectus et ante. Sed accumsan sollicitudin sapien, sit amet adipiscing turpis gravida ac. Risus in magna varius commodo.</p>
    <a class="more">READ MORE&gt;&gt;</a>
  </article>
  <div class="abs" style="left:324px;top:47px;width:332px">
    <div class="mini" style="margin-top:0"><div class="photo" style="width:124px;height:128px;background:linear-gradient(135deg,#eef0f3,#7a8898)" role="img" aria-label="Laboratory test tubes"></div><div><h4>Lorem ipsum dolor sit amet, consectetur elit a</h4><div class="meta">Genetic Engineering | Article</div></div></div>
    <div class="mini" style="margin-top:30px"><div class="photo" style="width:124px;height:128px;background:linear-gradient(135deg,#c84a8a,#f0c0d8)" role="img" aria-label="Pipette dropping liquid into sample"></div><div><h4>Lorem ipsum dolor sit amet, consectetur elit a</h4><div class="meta">Genetic Engineering | Article</div></div></div>
    <div class="mini" style="margin-top:30px"><div class="photo" style="width:124px;height:128px;background:linear-gradient(135deg,#e9eef2,#9aa7b3)" role="img" aria-label="Scientist examining a sample"></div><div><h4>Lorem ipsum dolor sit amet, consectetur elit a</h4><div class="meta">Genetic Engineering | Article</div></div></div>
  </div>
</section>

<aside class="abs" style="left:802px;top:300px;width:298px">
  <div style="font-size:14px;font-weight:600;color:var(--ink)">SEARCH:</div>
  <div style="display:flex;margin-top:8px"><div style="flex:1;height:34px;border:1px solid #ccc"></div>
    <div style="width:34px;height:34px;background:var(--red)"><svg width="34" height="34"><circle cx="15" cy="15" r="6" fill="none" stroke="#fff" stroke-width="2"/><line x1="19" y1="19" x2="25" y2="25" stroke="#fff" stroke-width="2.5"/></svg></div></div>
  <div class="side-panel" style="margin-top:18px;padding:14px">
    <div style="font-size:14px;font-weight:600;color:var(--ink)">SIGN UP</div>
    <div style="font-size:12px;margin-top:6px">To upload articles, bookmark, comments..</div>
    <div style="font-size:12px;color:var(--red);font-weight:600;margin-top:6px">FIND OUT MORE &gt;&gt;</div>
  </div>
  <div style="margin-top:18px;height:240px;width:215px;position:relative;background:linear-gradient(160deg,#f3f3f3 40%,#e85a2a)" role="img" aria-label="Music single advertisement with singer portrait">
    <div style="position:absolute;left:12px;top:14px;font-size:15px;font-weight:700;color:#222;line-height:19px">New Single<br>SLOW TIDE<br>on Tunebox<br>and Streamhall</div>
    <div style="position:absolute;left:12px;bottom:12px;font-size:28px;font-weight:700;color:#c8281c">VELO MARR</div>
  </div>
</aside>

<section class="abs" style="left:100px;top:851px;width:656px;display:flex;gap:29px">
  <article class="card" style="width:313px"><div class="shead"><h2>Biology</h2><div class="rule"></div></div>
    <div class="photo" style="height:173px;margin-top:18px;background:linear-gradient(135deg,#8c7d5a,#c9b98e)" role="img" aria-label="Hand holding plant seeds"></div>
    <h3>Wormholes in Host Defense: How Helminths Manipulate Host Tissues to Survive and Reproduce..</h3>
    <div class="meta">Genetic Engineering | Article | <b>By R.Ellison</b></div>
    <p>Aliquam molestie, mi et imperdiet euismod, dui purus auctor tellus, et interdum lacus lectus et ante. Sed accumsan sollicitudin sapien, sit amet adipiscing turpis gravida ac. Risus in magna varius commodo. Sed semper viverra egestas. Etiam pretium porttitor lectus, vel ornare neque porta volutpat.Sed semper viverra egestas.</p>
    <a class="more">READ MORE&gt;&gt;</a></article>
  <article class="card" style="width:314px"><div class="shead"><h2>Chemistry</h2><div class="rule"></div></div>
    <div class="photo" style="height:173px;margin-top:18px;background:linear-gradient(135deg,#f4a020,#3a7fc0)" role="img" aria-label="Molecular structure pattern in orange and blue"></div>
    <h3>Wormholes in Host Defense: How Helminths Manipulate Host Tissues to Survive and Reproduce..</h3>
    <div class="meta">Genetic Engineering | Article | <b>By R.Ellison</b></div>
    <p>Aliquam molestie, mi et imperdiet euismod, dui purus auctor tellus, et interdum lacus lectus et ante. Sed accumsan sollicitudin sapien, sit amet adipiscing turpis gravida ac. Risus in magna varius commodo. Sed semper viverra egestas. Etiam pretium porttitor lectus, vel ornare neque porta volutpat.Sed semper viverra egestas.</p>
    <a class="more">READ MORE&gt;&gt;</a></article>
</section>
<aside class="abs side-panel" style="left:785px;top:851px;width:315px;height:560px">
  <div class="shead"><h2>Most Popular</h2><div class="rule"></div></div>
  <div class="mini"><div class="photo" style="background:radial-gradient(circle,#8a6fe0,#1a1a4a)" role="img" aria-label="Glowing neuron network"></div><div><h4>Lorem ipsum dolor sit amet, consectetur elit</h4><div class="meta">Genetic Engineering | Article</div></div></div>
  <div class="mini"><div class="photo" style="background:linear-gradient(135deg,#f2f2f2,#c05070)" role="img" aria-label="Hand reaching toward light"></div><div><h4>Lorem ipsum dolor sit amet, consectetur elit</h4><div class="meta">Genetic Engineering | Article</div></div></div>
  <div class="mini"><div class="photo" style="background:linear-gradient(135deg,#fff,#6a9ad8)" role="img" aria-label="Molecule model illustration"></div><div><h4>Lorem ipsum dolor sit amet, consectetur elit</h4><div class="meta">Genetic Engineering | Article</div></div></div>
  <div class="mini"><div class="photo" style="background:radial-gradient(circle,#4a8ac0,#1c2a3a)" role="img" aria-label="Close-up of a human eye"></div><div><h4>Lorem ipsum dolor sit amet, consectetur elit</h4><div class="meta">Genetic Engineering | Article</div></div></div>
</aside>

<section class="abs sponsored">
  <div style="margin:32px 100px 0">
    <div class="shead"><h2>Sponsored</h2><div class="rule"></div></div>
    <div class="sp-grid">
      <div class="sp-item"><div class="photo" style="background:linear-gradient(135deg,#ddd,#6a5a50)" role="img" aria-label="Researcher looking through a microscope"></div><p>Duis convallis nec arcu at mollis. Aliquam eu dolor auctor, iris tique diam at, varius elit.</p><div class="by">Genetic engineering / Article by R.Ellison</div></div>
      <div class="sp-item"><div class="photo" style="background:linear-gradient(135deg,#5a6a80,#d8dde4)" role="img" aria-label="Athlete training in a gym"></div><p>Duis convallis nec arcu at mollis. Aliquam eu dolor auctor, iris tique diam at, varius elit.</p><div class="by">Genetic engineering / Article by R.Ellison</div></div>
      <div class="sp-item"><div class="photo" style="background:linear-gradient(135deg,#f5d040,#a87020)" role="img" aria-label="Woman stretching in sunlight"></div><p>Duis convallis nec arcu at mollis. Aliquam eu dolor auctor, iris tique diam at, varius elit.</p><div class="by">Genetic engineering / Article by R.Ellison</div></div>
      <div class="sp-item"><div class="photo" style="background:linear-gradient(135deg,#f0e4d8,#c8a088)" role="img" aria-label="Group of babies sitting together"></div><p>Duis convallis nec arcu at mollis. Aliquam eu dolor auctor, iris tique diam at, varius elit.</p><div class="by">Genetic engineering / Article by R.Ellison</div></div>
    </div>
  </div>
</section>

<section class="abs" style="left:100px;top:1861px;width:656px;display:flex;gap:29px">
  <article class="card" style="width:313px"><div class="shead"><h2>Physics</h2><div class="rule"></div></div>
    <div class="photo" style="height:173px;margin-top:18px;background:radial-gradient(circle at 50% 40%,#9aa0a8,#1e2024)" role="img" aria-label="Figure in a burst of smoke and debris"></div>
    <h3>Wormholes in Host Defense: How Helminths Manipulate Host Tissues to Survive and Reproduce..</h3>
    <div class="meta">Genetic Engineering | Article | <b>By R.Ellison</b></div>
    <p>Aliquam molestie, mi et imperdiet euismod, dui purus auctor tellus, et interdum lacus lectus et ante. Sed accumsan sollicitudin sapien, sit amet adipiscing turpis gravida ac. Risus in magna varius commodo. Sed semper viverra egestas. Etiam pretium porttitor lectus, vel ornare neque porta volutpat.Sed semper viverra egestas.</p>
    <a class="more">READ MORE&gt;&gt;</a></article>
  <article class="card" style="width:314px"><div class="shead"><h2>Computation</h2><div class="rule"></div></div>
    <div class="photo" style="height:173px;margin-top:18px;background:linear-gradient(135deg,#0a3a7a,#3aa0e8)" role="img" aria-label="Blue circuit board"></div>
    <h3>Wormholes in Host Defense: How Helminths Manipulate Host Tissues to Survive and Reproduce..</h3>
    <div class="meta">Genetic Engineering | Article | <b>By R.Ellison</b></div>
    <p>Aliquam molestie, mi et imperdiet euismod, dui purus auctor tellus, et interdum lacus lectus et ante. Sed accumsan sollicitudin sapien, sit amet adipiscing turpis gravida ac. Risus in magna varius commodo. Sed semper viverra egestas. Etiam pretium porttitor lectus, vel ornare neque porta volutpat.Sed semper viverra egestas.</p>
    <a class="more">READ MORE&gt;&gt;</a></article>
</section>
<aside class="abs" style="left:788px;top:1870px;width:312px;height:265px;background:linear-gradient(135deg,#8a1a3a,#2a0a18)" role="img" aria-label="Fashion advertisement with a couple">
  <div style="position:absolute;left:14px;top:110px;color:#fff;font-size:20px;font-weight:700;line-height:24px">LATE<br>BLOOM</div>
  <div style="position:absolute;left:0;bottom:0;width:312px;height:50px;background:#fff;display:flex;align-items:center;justify-content:space-between;padding:0 12px">
    <span style="font-size:18px;font-weight:700;color:#d8262c">Drapeline</span><span style="background:#d8262c;color:#fff;font-size:12px;font-weight:700;padding:5px 10px">BUY NOW</span>
  </div>
</aside>

<section class="abs" style="left:100px;top:2524px;width:656px;display:flex;gap:29px">
  <article class="card" style="width:313px"><div class="shead"><h2>Earth</h2><div class="rule"></div></div>
    <div class="photo" style="height:173px;margin-top:18px;background:linear-gradient(160deg,#0a1e3a,#d8a040)" role="img" aria-label="Earth from orbit with city lights"></div>
    <h3>Wormholes in Host Defense: How Helminths Manipulate Host Tissues to Survive and Reproduce..</h3>
    <div class="meta">Genetic Engineering | Article | <b>By R.Ellison</b></div>
    <p>Aliquam molestie, mi et imperdiet euismod, dui purus auctor tellus, et interdum lacus lectus et ante. Sed accumsan sollicitudin sapien, sit amet adipiscing turpis gravida ac. Risus in magna varius commodo. Sed semper viverra egestas. Etiam pretium porttitor lectus, vel ornare neque porta volutpat.Sed semper viverra egestas.</p>
    <a class="more">READ MORE&gt;&gt;</a></article>
  <article class="card" style="width:314px"><div class="shead"><h2>Technology</h2><div class="rule"></div></div>
    <div class="photo" style="height:173px;margin-top:18px;background:radial-gradient(circle,#9ac8e8,#1a2a3e)" role="img" aria-label="Hand touching floating interface icons"></div>
    <h3>Wormholes in Host Defense: How Helminths Manipulate Host Tissues to Survive and Reproduce..</h3>
    <div class="meta">Genetic Engineering | Article | <b>By R.Ellison</b></div>
    <p>Aliquam molestie, mi et imperdiet euismod, dui purus auctor tellus, et interdum lacus lectus et ante. Sed accumsan sollicitudin sapien, sit amet adipiscing turpis gravida ac. Risus in magna varius commodo. Sed semper viverra egestas. Etiam pretium porttitor lectus, vel ornare neque porta volutpat.Sed semper viverra egestas.</p>
    <a class="more">READ MORE&gt;&gt;</a></article>
</section>
<aside class="abs side-panel" style="left:785px;top:2524px;width:315px;height:560px">
  <div class="shead"><h2>Recommended</h2><div class="rule"></div></div>
  <div class="mini"><div class="photo" style="background:linear-gradient(135deg,#f0e8d8,#b89060)" role="img" aria-label="Glass of water with sunlight"></div><div><h4>Lorem ipsum dolor sit amet, consectetur elit</h4><div class="meta">Genetic Engineering | Article</div></div></div>
  <div class="mini"><div class="photo" style="background:linear-gradient(135deg,#6a3a2a,#e8a870)" role="img" aria-label="Hands holding a lit bulb"></div><div><h4>Lorem ipsum dolor sit amet, consectetur elit</h4><div class="meta">Genetic Engineering | Article</div></div></div>
  <div class="mini"><div class="photo" style="background:linear-gradient(135deg,#f4f4f4,#9aa4b0)" role="img" aria-label="White humanoid robot"></div><div><h4>Lorem ipsum dolor sit amet, consectetur elit</h4><div class="meta">Genetic Engineering | Article</div></div></div>
  <div class="mini"><div class="photo" style="background:linear-gradient(135deg,#1a3a4a,#5ab0c8)" role="img" aria-label="Digital data visualization"></div><div><h4>Lorem ipsum dolor sit amet, consectetur elit</h4><div class="meta">Genetic Engineering | Article</div></div></div>
</aside>

<section class="abs" style="left:100px;top:3202px;width:1000px;display:flex;gap:29px">
  <article class="card" style="width:314px"><div class="shead"><h2>Health</h2><div class="rule"></div></div>
    <div class="photo" style="height:173px;margin-top:18px;background:linear-gradient(180deg,#e8ecef,#b8c4cc)" role="img" aria-label="Person meditating by the sea"></div>
    <h3>Wormholes in Host Defense: How Helminths Manipulate Host Tissues to Survive and Reproduce..</h3>
    <div class="meta">Genetic Engineering | Article | <b>By R.Ellison</b></div>
    <p>Aliquam molestie, mi et imperdiet euismod, dui purus auctor tellus, et interdum lacus lectus et ante. Sed accumsan sollicitudin sapien, sit amet adipiscing turpis gravida ac. Risus in magna varius commodo. Sed semper viverra egestas. Etiam pretium porttitor lectus, vel ornare neque porta volutpat.Sed semper viverra egestas.</p>
    <a class="more">READ MORE&gt;&gt;</a></article>
  <article class="card" style="width:314px"><div class="shead"><h2>Social</h2><div class="rule"></div></div>
    <div class="photo" style="height:173px;margin-top:18px;background:linear-gradient(180deg,#c8c0b8,#4a3e36)" role="img" aria-label="Large crowd of people"></div>
    <h3>Wormholes in Host Defense: How Helminths Manipulate Host Tissues to Survive and Reproduce..</h3>
    <div class="meta">Genetic Engineering | Article | <b>By R.Ellison</b></div>
    <p>Aliquam molestie, mi et imperdiet euismod, dui purus auctor tellus, et interdum lacus lectus et ante. Sed accumsan sollicitudin sapien, sit amet adipiscing turpis gravida ac. Risus in magna varius commodo. Sed semper viverra egestas. Etiam pretium porttitor lectus, vel ornare neque porta volutpat.Sed semper viverra egestas.</p>
    <a class="more">READ MORE&gt;&gt;</a></article>
  <article class="card" style="width:314px"><div class="shead"><h2>Other</h2><div class="rule"></div></div>
    <div class="photo" style="height:173px;margin-top:18px;background:linear-gradient(180deg,#7a8a88,#2e3a36)" role="img" aria-label="Fish swimming underwater"></div>
    <h3>Wormholes in Host Defense: How Helminths Manipulate Host Tissues to Survive and Reproduce..</h3>
    <div class="meta">Genetic Engineering | Article | <b>By R.Ellison</b></div>
    <p>Aliquam molestie, mi et imperdiet euismod, dui purus auctor tellus, et interdum lacus lectus et ante. Sed accumsan sollicitudin sapien, sit amet adipiscing turpis gravida ac. Risus in magna varius commodo. Sed semper viverra egestas. Etiam pretium porttitor lectus, vel ornare neque porta volutpat.Sed semper viverra egestas.</p>
    <a class="more">READ MORE&gt;&gt;</a></article>
</section>

<section class="abs" style="left:100px;top:3866px;width:1000px">
  <div style="font-size:22px;font-weight:600;color:var(--red)">VISIT ALSO</div>
  <div class="partners">
    <div class="chip">Clipsaver</div><span>dealnest</span><span>ThriftPoint</span><span>bluefig</span><span>Cartwave</span><span>PennyPath</span>
  </div>
</section>

<footer class="abs footer">
  <div style="display:flex;margin:28px 100px 0">
    <div style="width:520px"><h5>Quick Links</h5>
      <div class="links">
        <ul><li>Latest</li><li>Biology</li><li>Chemistry</li><li>Physics</li><li>Computation</li><li>Earth</li></ul>
        <ul><li>Technology</li><li>Health</li><li>Social</li><li>More News?</li><li>Questions?</li><li>Support</li></ul>
        <ul><li>Privacy Policy</li><li>Terms of use</li><li>FAQ</li><li>Enquiry</li><li>Unsubscribe</li><li>Legal Notice</li></ul>
        <ul><li>Register</li><li>Login</li><li>Search</li></ul>
      </div></div>
    <div style="width:280px;border-left:1px solid #ddd;padding-left:24px"><h5>Email Signup</h5>
      <div class="field">Name</div><div class="field">Email ID</div><span class="submit">SUBMIT</span></div>
    <div style="border-left:1px solid #ddd;padding-left:24px"><h5>Connect with us</h5>
      <ul class="social">
        <li><i></i>Join with us on <b>Circlehall</b></li>
        <li><i style="background:#3fa9dc"></i>Follow us on <b>Chirpline</b></li>
        <li><i style="background:#2a6ea8"></i>Share on <b>Workweave</b></li>
        <li><i style="background:#c8302a"></i>Watch on <b style="color:#c8302a">Reelstream</b></li>
      </ul></div>
  </div>
</footer>
<div class="abs bottom">Copyright © 2014 &nbsp; Quarry Lantern Works gGmbH. &nbsp; All rights reserved.</div>

</body>
</html>
```